A new novel about the early days of The Marlows needs a book cover design

The title of the book is A LANTERN IN WINTER
The cover should also include "a novel" and "by Tom Holloway" Those can be together or separate.
The design element I'd like to incorporate is the iconic "Dock Wall" photo of The Marlows in 1960, which I've attached below. Since we're not sure if we can get the rights to the actual photo, it's probably best if the design merely references that photo, or distorts it in an interesting way. But it should be very clear that the book is about the Marlows.
The novel is in many ways based on that photo and evokes the city of Hamburg in 1960, which was gritty, raw, and sexually charged (as were The Marlows).
The tone of the novel is romantic, passionate, and very funny - but never broad and silly.

```html
<!DOCTYPE html>
<html lang="en">
<head>
<meta charset="utf-8">
<title>A Lantern in Winter — Cover</title>
<link rel="stylesheet" href="https://fonts.googleapis.com/css2?family=Rye&family=Francois+One&family=Jost:wght@600&display=swap">
<style>
  :root {
    --paper: #ffffff;
    --ink: #000000;
    --gold: #d4b06a;
    --maroon: #7e2228;
    --white: #ffffff;
  }
  html, body {
    margin: 0;
    padding: 0;
    width: 1200px;
    height: 1200px;
    overflow: hidden;
    background: var(--paper);
  }
  .canvas {
    position: relative;
    width: 1200px;
    height: 1200px;
  }
  .cover, .strip {
    position: absolute;
    display: block;
  }
  .cover { left: 30px; top: 17px; }
  .strip { left: 800px; top: 17px; }
  .kicker { font-family: "Jost", sans-serif; font-weight: 600; letter-spacing: 1px; }
  .author { font-family: "Francois One", sans-serif; }
  .title { font-family: "Rye", serif; }
</style>
</head>
<body>
<main class="canvas">

  <svg class="cover" width="726" height="1163" viewBox="0 0 726 1163" aria-label="Front cover">
    <defs>
      <linearGradient id="tone-olive" x1="0" y1="0" x2="0" y2="1">
        <stop offset="0" stop-color="#c9cb9c"/>
        <stop offset="0.3" stop-color="#8f9262"/>
        <stop offset="0.55" stop-color="#4e5130"/>
        <stop offset="0.8" stop-color="#6d7046"/>
        <stop offset="1" stop-color="#8d8f64"/>
      </linearGradient>
      <linearGradient id="tone-teal" x1="0" y1="0" x2="0" y2="1">
        <stop offset="0" stop-color="#9cc7c4"/>
        <stop offset="0.3" stop-color="#5d8f8c"/>
        <stop offset="0.55" stop-color="#264c4a"/>
        <stop offset="0.8" stop-color="#3f6a67"/>
        <stop offset="1" stop-color="#5d8985"/>
      </linearGradient>
      <linearGradient id="tone-rose" x1="0" y1="0" x2="0" y2="1">
        <stop offset="0" stop-color="#eab3ae"/>
        <stop offset="0.3" stop-color="#a9605e"/>
        <stop offset="0.55" stop-color="#5a2222"/>
        <stop offset="0.8" stop-color="#7e3a38"/>
        <stop offset="1" stop-color="#b57a73"/>
      </linearGradient>
      <linearGradient id="tone-violet" x1="0" y1="0" x2="0" y2="1">
        <stop offset="0" stop-color="#a99ac2"/>
        <stop offset="0.3" stop-color="#66568a"/>
        <stop offset="0.55" stop-color="#241a38"/>
        <stop offset="0.8" stop-color="#3e3158"/>
        <stop offset="1" stop-color="#7d7095"/>
      </linearGradient>
      <linearGradient id="tone-umber" x1="0" y1="0" x2="0" y2="1">
        <stop offset="0" stop-color="#efcca4"/>
        <stop offset="0.3" stop-color="#ad7d52"/>
        <stop offset="0.55" stop-color="#4e2f16"/>
        <stop offset="0.8" stop-color="#6e4524"/>
        <stop offset="1" stop-color="#9a6d47"/>
      </linearGradient>
    </defs>

    <rect class="cover-ground" x="0" y="0" width="726" height="1163" fill="var(--ink)"/>
    <rect class="cover-tab" x="675" y="113" width="51" height="182" fill="var(--gold)"/>

    <g class="band-photo" role="img" aria-label="Photo of the five band members posing with guitars and drums by the dock wall, split into five tinted vertical stripes">
      <rect x="0"   y="365" width="151" height="534" fill="url(#tone-olive)"/>
      <rect x="155" y="365" width="149" height="534" fill="url(#tone-teal)"/>
      <rect x="310" y="365" width="140" height="534" fill="url(#tone-rose)"/>
      <rect x="456" y="365" width="138" height="534" fill="url(#tone-violet)"/>
      <rect x="599" y="365" width="127" height="534" fill="url(#tone-umber)"/>
    </g>

    <text class="kicker" x="167" y="183" font-size="27" fill="var(--gold)">A NOVEL BY</text>
    <text class="author" x="439" y="195" font-size="68" fill="var(--white)">TOM</text>
    <text class="author" x="167" y="276" font-size="68" fill="var(--white)" textLength="390" lengthAdjust="spacingAndGlyphs">HOLLOWAY</text>

    <text class="title" x="114" y="890" font-size="150" fill="var(--ink)" stroke="var(--white)" stroke-width="2" textLength="506" lengthAdjust="spacingAndGlyphs">A LANTERN</text>
    <text class="title" x="72" y="1035" font-size="128" fill="var(--white)" textLength="584" lengthAdjust="spacingAndGlyphs">IN WINTER</text>
  </svg>

  <svg class="strip" width="350" height="1163" viewBox="0 0 350 1163" aria-label="Bookmark strip">
    <rect class="strip-band" x="53" y="0" width="248" height="1163" fill="var(--gold)"/>
    <text class="kicker" x="70" y="202" font-size="20" fill="var(--maroon)">A NOVEL BY</text>
    <text class="author" x="218" y="208" font-size="40" fill="var(--ink)">TOM</text>
    <text class="author" x="68" y="253" font-size="40" fill="var(--ink)" textLength="217" lengthAdjust="spacingAndGlyphs">HOLLOWAY</text>
    <text class="title" x="64" y="352" font-size="64" fill="var(--maroon)" textLength="226" lengthAdjust="spacingAndGlyphs">A LANTERN</text>
    <text class="title" x="68" y="430" font-size="64" fill="var(--maroon)" textLength="218" lengthAdjust="spacingAndGlyphs">IN WINTER</text>
  </svg>

</main>
</body>
</html>
```